Killer design for artists website and gallery

Current website is www.bluemoorstudio.com.au and it runs on a very simple Wordpress standard theme. We would like a theme designed and customised to suit the branding and style. We have someone who will then code the site in HTML and CSS into Wordpress.

The general theme and branding can be seen on the site at the moment. Please note I have now uploaded full size files into the project. The website background files are for reference only as they are currently on the site. There is no requirement to use them in the new design, however the logo must be as per the attachment.. Please submit a home page/main gallery, and we will request additional pages (about us, other galleries etc.) from those designers we like during the project time.
Updates

Please note I have now uploaded full size files into the project. The website background files are for reference only as they are currently on the site. There is no requirement to use them in the new design, however the logo must be as per the attachment.

Target Market(s)

sales are only in Australia, and priced between approx $100 and $1000. Most viewers and buyers are 20-40 years old, and looking for a casual canvas work for home, or a gift.

Industry/Entity Type

Artists

Font styles to use
Serif
Sans Serif

Requirements
Must have
• gallery of images, responsive design, ability to select categories of pictures (see top menu on current site) and have the gallery change to match, colours to match branding and logo.
Nice to have
• simple minimalist style is preferred. More like http://www.tobiasmerrow.com/ than http://www.harbourpaintco.com.au/ or http://www.velvetcanvas.com.au/
Should not have
• does not need any online store, or shopping cart etc.

```html
<!DOCTYPE html>
<html lang="en">
<head>
<meta charset="utf-8">
<title>Bluemoor Art — Canvas Art</title>
<link rel="stylesheet" href="https://fonts.googleapis.com/css2?family=Open+Sans:wght@400;600;700&display=swap">
<style>
:root{
  --bg:#f4f4f4;
  --page:#ffffff;
  --ink:#444444;
  --ink-soft:#777777;
  --ink-faint:#9a9a9a;
  --rule:#e4e4e4;
  --accent:#f5c400;
  --link:#2d6aa0;
  --field:#efefef;
  --star-off:#8a8a8a;
}
*{box-sizing:border-box}
html,body{margin:0;padding:0;overflow:hidden}
body{font-family:"Open Sans",Arial,sans-serif;color:var(--ink);background:var(--bg)}
.canvas{position:relative;width:1200px;height:3061px;overflow:hidden;background:var(--bg)}
.branch{position:absolute}
.branch-left{left:-60px;top:230px;width:300px;height:460px;background:radial-gradient(ellipse at 30% 45%,rgba(70,70,70,.28),rgba(70,70,70,0) 65%)}
.branch-right{left:990px;top:110px;width:270px;height:580px;background:radial-gradient(ellipse at 60% 40%,rgba(240,214,40,.45),rgba(240,214,40,0) 65%)}
.page{position:absolute;left:188px;top:0;width:824px;height:2960px;background:var(--page)}
.abs{position:absolute}

/* header */
.brand{position:absolute;left:198px;top:84px;display:flex;align-items:center;gap:8px}
.brand-mark{width:26px;height:26px;background:#1b1b1b;border-radius:4px}
.brand-name{font-weight:700;font-size:17px;color:#1b1b1b}
.main-nav{position:absolute;top:107px;left:333px;font-size:13px;font-weight:700;color:#555}
.main-nav a{position:absolute;white-space:nowrap;color:inherit;text-decoration:none}
.main-nav a.is-current{color:var(--accent)}

.hero{position:absolute;left:198px;top:149px;width:806px;height:325px;
  background:linear-gradient(90deg,#3c5b55 0%,#c98a1e 18%,#f0b62c 40%,#e59a1f 65%,#b8771c 84%,#355a58 100%)}
.hero-title{position:absolute;left:545px;top:376px;font-size:21px;font-weight:700;color:#fff;white-space:nowrap}
.hero-arrows{position:absolute;left:923px;top:418px}

.section-title{position:absolute;left:194px;top:526px;margin:0;font-size:22px;font-weight:700;color:#555}

/* posts */
.posts{position:absolute;left:196px;top:568px;width:531px}
.post{position:relative;height:470px}
.post-title{position:absolute;left:0;top:0;margin:0;font-size:15px;font-weight:700;color:#444}
.rating{position:absolute;right:0;top:2px;display:flex;align-items:center;gap:3px;font-size:11px;color:var(--ink-soft)}
.rating span{margin-right:8px}
.rule{position:absolute;left:0;width:100%;height:1px;background:var(--rule)}
.post-meta{position:absolute;left:0;top:30px;display:flex;align-items:center;gap:6px;font-size:11px;color:var(--ink-soft)}
.post-meta .sep{color:#bbb}
.post-image{position:absolute;left:0;top:71px;width:531px;height:227px}
.post-excerpt{position:absolute;left:0;top:306px;margin:0;font-size:10.6px;line-height:15px;color:#666}
.share-row{position:absolute;left:0;top:383px;width:100%;display:flex;align-items:center;font-size:11px;font-weight:700;color:#444}
.share-row .label{margin-right:8px}
.pill{display:inline-block;height:15px;line-height:13px;padding:0 5px;margin-right:4px;border:1px solid #c9d3de;border-radius:2px;font-size:9px;font-weight:600;color:#3a5a80;background:#f5f8fb}
.like-this{margin-left:auto;display:flex;align-items:center;gap:8px}
.like-btn{display:inline-block;height:17px;line-height:17px;padding:0 6px;background:var(--accent);font-size:9px;font-weight:700;color:#333}

.img-rocks{background:linear-gradient(180deg,#7fa7cf 0%,#a9c3dc 45%,#7b4a35 70%,#9fb7c9 100%)}
.img-table{background:linear-gradient(135deg,#9a8b76 0%,#5f6567 40%,#b8a28a 70%,#7d6f62 100%)}
.img-umbrella{background:linear-gradient(180deg,#3d5b80 0%,#4b6f95 50%,#2f4d70 100%)}
.img-huts{background:linear-gradient(180deg,#2c4f8a 0%,#6f86b8 55%,#c49a5a 80%,#a8793d 100%)}
.img-sea{background:linear-gradient(180deg,#e8ecef 0%,#7fa1c8 35%,#2f6aa8 70%,#1d4f86 100%)}

/* pagination */
.pager{position:absolute;left:376px;top:2908px;display:flex;align-items:center;gap:11px;font-size:10px;color:#999}
.pager .pg{width:22px;height:20px;line-height:20px;text-align:center;background:#ececec}
.pager .pg.is-current{background:var(--accent);color:#333}
.pager .arrow{font-size:16px;color:#333;font-weight:700}
.pager .gap{width:14px;text-align:center}

/* sidebar */
.sidebar{position:absolute;left:747px;top:0;width:257px}
.widget-title{position:absolute;left:747px;margin:0;font-size:12px;font-weight:700;color:#444}
.widget-rule{position:absolute;left:747px;width:257px;height:1px;background:var(--rule)}
.field{position:absolute;left:747px;width:257px;height:29px;background:var(--field);font-size:10px;color:#888;padding:8px 7px}
.side-text{position:absolute;left:747px;width:257px;font-size:10.5px;line-height:17px;color:#666;margin:0}
.side-text a{color:var(--link);text-decoration:none}
.side-list{position:absolute;left:747px;margin:0;padding:0;list-style:none;font-size:11px;color:#666}
.side-list li{height:var(--step);line-height:var(--step)}

.social-box{position:absolute;left:747px;top:643px;width:257px;height:239px;border:1px solid #a9b7cc;background:#fff}
.social-head{height:24px;background:#edf0f5;border-bottom:1px solid #c4cde0;font-size:10px;font-weight:700;color:#333;padding:5px 8px}
.social-page{display:flex;gap:8px;padding:8px}
.social-thumb{width:36px;height:36px;background:#3c4f6e}
.social-name{font-size:12px;font-weight:700;color:var(--link)}
.social-like{display:inline-block;margin-top:3px;height:15px;line-height:13px;padding:0 5px;border:1px solid #c9d3de;font-size:9px;color:#3a5a80;background:#f5f8fb}
.social-count{font-size:9.5px;color:#555;padding:0 8px;margin:2px 0 4px}
.fans{display:grid;grid-template-columns:repeat(5,42px);gap:4px 9px;padding:0 8px}
.fan{text-align:center;font-size:8px;color:#666}
.fan i{display:block;width:42px;height:40px;background:#9aa3ad}
.social-foot{position:absolute;left:8px;bottom:3px;font-size:8px;color:#777}

.follow-btn{position:absolute;left:747px;top:1470px;height:17px;line-height:15px;padding:0 6px;border:1px solid #b8c4d0;border-radius:3px;font-size:9px;font-weight:600;color:#333;background:#eef2f6}

/* footer */
.footer-nav{position:absolute;top:2990px;left:0;width:1200px;text-align:center;font-size:11px;color:#666;word-spacing:2px}
.footer-nav .sep{color:#aaa;margin:0 10px}
.copyright{position:absolute;top:3028px;left:0;width:1200px;text-align:center;font-size:11px;color:#666}
</style>
</head>
<body>
<div class="canvas">

  <div class="branch branch-left" role="img" aria-label="Dark painted tree branch decoration"></div>
  <div class="branch branch-right" role="img" aria-label="Yellow painted tree branch decoration"></div>

  <div class="page"></div>

  <header>
    <div class="brand"><span class="brand-mark"></span><span class="brand-name">Bluemoor Art</span></div>
    <nav class="main-nav">
      <a class="is-current" style="left:0">Home</a>
      <a style="left:65px">About</a>
      <a style="left:140px">Cityscapes</a>
      <a style="left:234px">Other Works</a>
      <a style="left:334px">Seascapes</a>
      <a style="left:443px">Testimonials</a>
      <a style="left:553px">Works for Sale</a>
    </nav>
  </header>

  <div class="hero" role="img" aria-label="Painting of a twisted tree against a glowing orange sky"></div>
  <div class="hero-title">Beautiful Canvas Art Made in Melbourne</div>
  <svg class="hero-arrows" width="50" height="28" viewBox="0 0 50 28">
    <polyline points="18,4 8,14 18,24" fill="none" stroke="#f5c400" stroke-width="4"/>
    <polyline points="32,4 42,14 32,24" fill="none" stroke="#ffffff" stroke-width="4"/>
  </svg>

  <h1 class="section-title">Canvas Art</h1>

  <svg width="0" height="0" style="position:absolute">
    <defs>
      <polygon id="star" points="7,0 9,5 14,5.3 10.2,8.6 11.4,13.6 7,10.9 2.6,13.6 3.8,8.6 0,5.3 5,5"/>
    </defs>
  </svg>

  <main class="posts">
    <article class="post">
      <h2 class="post-title">North Melbourne Markets</h2>
      <div class="rating"><span>Rating :</span>
        <svg width="14" height="14"><use href="#star" fill="#f5c400"/></svg><svg width="14" height="14"><use href="#star" fill="#f5c400"/></svg><svg width="14" height="14"><use href="#star" fill="#f5c400"/></svg><svg width="14" height="14"><use href="#star" fill="#f5c400"/></svg><svg width="14" height="14"><use href="#star" fill="#8a8a8a"/></svg>
      </div>
      <div class="rule" style="top:20px"></div>
      <div class="post-meta">
        <svg width="14" height="14"><rect x="1" y="2" width="12" height="11" fill="#bdbdbd"/><rect x="1" y="2" width="12" height="3" fill="#8f8f8f"/></svg>
        <span>June 17, 2013</span><span class="sep">|</span>
        <svg width="12" height="12"><rect x="0" y="1" width="12" height="2" fill="#9a9a9a"/><rect x="0" y="5" width="12" height="2" fill="#9a9a9a"/><rect x="0" y="9" width="12" height="2" fill="#9a9a9a"/></svg>
        <span>Category : Art, market</span><span class="sep">|</span>
        <svg width="16" height="13"><ellipse cx="8" cy="6" rx="8" ry="5.5" fill="#b5b5b5"/><polygon points="3,9 2,13 7,10" fill="#b5b5b5"/></svg>
        <span>Leave a comment</span>
      </div>
      <div class="rule" style="top:55px"></div>
      <div class="post-image img-rocks" role="img" aria-label="Seascape painting of rock stacks under a blue sky"></div>
      <p class="post-excerpt">Lorem Ipsum is simply dummy text of the printing and typesetting industry. Lorem Ipsum has been the industry's standard dummy text ever since the 1500s, when an unknown printer took a galley of type and scrambled it to make a type specimen book.</p>
      <div class="rule" style="top:372px"></div>
      <div class="share-row"><span class="label">Share This :</span><span class="pill">Post</span><span class="pill">Like</span><span class="pill">+1</span>
        <span class="like-this">Like This : <span class="like-btn">★ Like</span></span></div>
      <div class="rule" style="top:412px"></div>
    </article>

    <article class="post">
      <h2 class="post-title">North Melbourne Markets</h2>
      <div class="rating"><span>Rating :</span>
        <svg width="14" height="14"><use href="#star" fill="#f5c400"/></svg><svg width="14" height="14"><use href="#star" fill="#f5c400"/></svg><svg width="14" height="14"><use href="#star" fill="#f5c400"/></svg><svg width="14" height="14"><use href="#star" fill="#f5c400"/></svg><svg width="14" height="14"><use href="#star" fill="#8a8a8a"/></svg>
      </div>
      <div class="rule" style="top:20px"></div>
      <div class="post-meta">
        <svg width="14" height="14"><rect x="1" y="2" width="12" height="11" fill="#bdbdbd"/><rect x="1" y="2" width="12" height="3" fill="#8f8f8f"/></svg>
        <span>June 17, 2013</span><span class="sep">|</span>
        <svg width="12" height="12"><rect x="0" y="1" width="12" height="2" fill="#9a9a9a"/><rect x="0" y="5" width="12" height="2" fill="#9a9a9a"/><rect x="0" y="9" width="12" height="2" fill="#9a9a9a"/></svg>
        <span>Category : Art, market</span><span class="sep">|</span>
        <svg width="16" height="13"><ellipse cx="8" cy="6" rx="8" ry="5.5" fill="#b5b5b5"/><polygon points="3,9 2,13 7,10" fill="#b5b5b5"/></svg>
        <span>Leave a comment</span>
      </div>
      <div class="rule" style="top:55px"></div>
      <div class="post-image img-table" role="img" aria-label="Market stall table laid out with price tags and art supplies"></div>
      <p class="post-excerpt">Lorem Ipsum is simply dummy text of the printing and typesetting industry. Lorem Ipsum has been the industry's standard dummy text ever since the 1500s, when an unknown printer took a galley of type and scrambled it to make a type specimen book.</p>
      <div class="rule" style="top:372px"></div>
      <div class="share-row"><span class="label">Share This :</span><span class="pill">Post</span><span class="pill">Like</span><span class="pill">+1</span>
        <span class="like-this">Like This : <span class="like-btn">★ Like</span></span></div>
      <div class="rule" style="top:412px"></div>
    </article>

    <article class="post">
      <h2 class="post-title">North Melbourne Markets</h2>
      <div class="rating"><span>Rating :</span>
        <svg width="14" height="14"><use href="#star" fill="#f5c400"/></svg><svg width="14" height="14"><use href="#star" fill="#f5c400"/></svg><svg width="14" height="14"><use href="#star" fill="#f5c400"/></svg><svg width="14" height="14"><use href="#star" fill="#f5c400"/></svg><svg width="14" height="14"><use href="#star" fill="#8a8a8a"/></svg>
      </div>
      <div class="rule" style="top:20px"></div>
      <div class="post-meta">
        <svg width="14" height="14"><rect x="1" y="2" width="12" height="11" fill="#bdbdbd"/><rect x="1" y="2" width="12" height="3" fill="#8f8f8f"/></svg>
        <span>June 17, 2013</span><span class="sep">|</span>
        <svg width="12" height="12"><rect x="0" y="1" width="12" height="2" fill="#9a9a9a"/><rect x="0" y="5" width="12" height="2" fill="#9a9a9a"/><rect x="0" y="9" width="12" height="2" fill="#9a9a9a"/></svg>
        <span>Category : Art, market</span><span class="sep">|</span>
        <svg width="16" height="13"><ellipse cx="8" cy="6" rx="8" ry="5.5" fill="#b5b5b5"/><polygon points="3,9 2,13 7,10" fill="#b5b5b5"/></svg>
        <span>Leave a comment</span>
      </div>
      <div class="rule" style="top:55px"></div>
      <div class="post-image img-umbrella" role="img" aria-label="Painting of a figure under an umbrella in blue rain"></div>
      <p class="post-excerpt">Lorem Ipsum is simply dummy text of the printing and typesetting industry. Lorem Ipsum has been the industry's standard dummy text ever since the 1500s, when an unknown printer took a galley of type and scrambled it to make a type specimen book.</p>
      <div class="rule" style="top:372px"></div>
      <div class="share-row"><span class="label">Share This :</span><span class="pill">Post</span><span class="pill">Like</span><span class="pill">+1</span>
        <span class="like-this">Like This : <span class="like-btn">★ Like</span></span></div>
      <div class="rule" style="top:412px"></div>
    </article>

    <article class="post">
      <h2 class="post-title">North Melbourne Markets</h2>
      <div class="rating"><span>Rating :</span>
        <svg width="14" height="14"><use href="#star" fill="#f5c400"/></svg><svg width="14" height="14"><use href="#star" fill="#f5c400"/></svg><svg width="14" height="14"><use href="#star" fill="#f5c400"/></svg><svg width="14" height="14"><use href="#star" fill="#f5c400"/></svg><svg width="14" height="14"><use href="#star" fill="#8a8a8a"/></svg>
      </div>
      <div class="rule" style="top:20px"></div>
      <div class="post-meta">
        <svg width="14" height="14"><rect x="1" y="2" width="12" height="11" fill="#bdbdbd"/><rect x="1" y="2" width="12" height="3" fill="#8f8f8f"/></svg>
        <span>June 17, 2013</span><span class="sep">|</span>
        <svg width="12" height="12"><rect x="0" y="1" width="12" height="2" fill="#9a9a9a"/><rect x="0" y="5" width="12" height="2" fill="#9a9a9a"/><rect x="0" y="9" width="12" height="2" fill="#9a9a9a"/></svg>
        <span>Category : Art, market</span><span class="sep">|</span>
        <svg width="16" height="13"><ellipse cx="8" cy="6" rx="8" ry="5.5" fill="#b5b5b5"/><polygon points="3,9 2,13 7,10" fill="#b5b5b5"/></svg>
        <span>Leave a comment</span>
      </div>
      <div class="rule" style="top:55px"></div>
      <div class="post-image img-huts" role="img" aria-label="Painting of a row of beach huts on sand"></div>
      <p class="post-excerpt">Lorem Ipsum is simply dummy text of the printing and typesetting industry. Lorem Ipsum has been the industry's standard dummy text ever since the 1500s, when an unknown printer took a galley of type and scrambled it to make a type specimen book.</p>
      <div class="rule" style="top:372px"></div>
      <div class="share-row"><span class="label">Share This :</span><span class="pill">Post</span><span class="pill">Like</span><span class="pill">+1</span>
        <span class="like-this">Like This : <span class="like-btn">★ Like</span></span></div>
      <div class="rule" style="top:412px"></div>
    </article>

    <article class="post">
      <h2 class="post-title">North Melbourne Markets</h2>
      <div class="rating"><span>Rating :</span>
        <svg width="14" height="14"><use href="#star" fill="#f5c400"/></svg><svg width="14" height="14"><use href="#star" fill="#f5c400"/></svg><svg width="14" height="14"><use href="#star" fill="#f5c400"/></svg><svg width="14" height="14"><use href="#star" fill="#f5c400"/></svg><svg width="14" height="14"><use href="#star" fill="#8a8a8a"/></svg>
      </div>
      <div class="rule" style="top:20px"></div>
      <div class="post-meta">
        <svg width="14" height="14"><rect x="1" y="2" width="12" height="11" fill="#bdbdbd"/><rect x="1" y="2" width="12" height="3" fill="#8f8f8f"/></svg>
        <span>June 17, 2013</span><span class="sep">|</span>
        <svg width="12" height="12"><rect x="0" y="1" width="12" height="2" fill="#9a9a9a"/><rect x="0" y="5" width="12" height="2" fill="#9a9a9a"/><rect x="0" y="9" width="12" height="2" fill="#9a9a9a"/></svg>
        <span>Category : Art, market</span><span class="sep">|</span>
        <svg width="16" height="13"><ellipse cx="8" cy="6" rx="8" ry="5.5" fill="#b5b5b5"/><polygon points="3,9 2,13 7,10" fill="#b5b5b5"/></svg>
        <span>Leave a comment</span>
      </div>
      <div class="rule" style="top:55px"></div>
      <div class="post-image img-sea" role="img" aria-label="Triptych of seascape canvases with small sailing boats"></div>
      <p class="post-excerpt">Lorem Ipsum is simply dummy text of the printing and typesetting industry. Lorem Ipsum has been the industry's standard dummy text ever since the 1500s, when an unknown printer took a galley of type and scrambled it to make a type specimen book.</p>
      <div class="rule" style="top:372px"></div>
      <div class="share-row"><span class="label">Share This :</span><span class="pill">Post</span><span class="pill">Like</span><span class="pill">+1</span>
        <span class="like-this">Like This : <span class="like-btn">★ Like</span></span></div>
      <div class="rule" style="top:412px"></div>
    </article>
  </main>

  <nav class="pager">
    <span class="arrow">‹</span>
    <span class="pg">1</span><span class="pg">2</span><span class="pg">3</span><span class="pg is-current">4</span><span class="pg">5</span>
    <span class="gap">…</span>
    <span class="pg">15</span><span class="pg">30</span><span class="pg">45</span>
    <span class="arrow">›</span>
  </nav>

  <!-- sidebar -->
  <h3 class="widget-title" style="top:564px">Search</h3>
  <div class="field" style="top:596px">Search</div>

  <div class="social-box">
    <div class="social-head">Find us online</div>
    <div class="social-page">
      <div class="social-thumb"></div>
      <div><div class="social-name">Bluemoor Studio</div><span class="social-like">Like</span></div>
    </div>
    <div class="social-count">2,911 people like Bluemoor Studio.</div>
    <div class="fans">
      <div class="fan"><i></i>Milo</div><div class="fan"><i></i>Remy</div><div class="fan"><i></i>Felix</div><div class="fan"><i></i>Nadia</div><div class="fan"><i></i>Lena</div>
      <div class="fan"><i></i>Ivo</div><div class="fan"><i></i>Tess</div><div class="fan"><i></i>Bruno</div><div class="fan"><i></i>Elio</div><div class="fan"><i></i>Reid</div>
    </div>
    <div class="social-foot">Social plugin</div>
  </div>

  <h3 class="widget-title" style="top:895px">Follow Blog via Email</h3>
  <div class="widget-rule" style="top:918px"></div>
  <p class="side-text" style="top:942px">Enter your email address to follow this blog and receive notifications of new posts by email.</p>
  <div class="field" style="top:994px">Enter Your E-Mail Address</div>
  <p class="side-text" style="top:1034px">Join 14 other followers</p>

  <h3 class="widget-title" style="top:1091px;padding-left:20px">Microfeed</h3>
  <svg class="abs" style="left:747px;top:1094px" width="14" height="14"><circle cx="7" cy="7" r="7" fill="#3ea6dd"/></svg>
  <div class="widget-rule" style="top:1114px"></div>
  <p class="side-text" style="top:1134px">Website just clicked over 1,000 views, huge thank you to everybody who's viewed, commented, rated and liked.<br>Look... <a>bm.ly/Qa71Kd, 7 months ago</a></p>
  <p class="side-text" style="top:1228px">Great to see everyone today. Stay tuned for the next market date.<br><a>7 months ago</a>, <a>Ready for action.</a><br><a>Come say hi :-) bm.ly/7Rt2Wp, 7 months ago</a></p>
  <p class="side-text" style="top:1341px">I posted a new photo to my page<br><a>bm.ly/K4m8Zs, 7 months ago</a></p>
  <p class="side-text" style="top:1402px">Getting ready and prepared for tomorrow at The North Melbourne Market.<br><a>7 months ago</a></p>
  <span class="follow-btn">Follow @username</span>

  <h3 class="widget-title" style="top:1530px">Recent Posts</h3>
  <div class="widget-rule" style="top:1554px"></div>
  <ul class="side-list" style="top:1573px;--step:33px">
    <li>North Melbourne Markets</li><li>Ready for North Melbourne Market Tomorrow</li><li>Wood and Trees</li><li>Into The Rain</li><li>My newest seascape</li>
  </ul>

  <h3 class="widget-title" style="top:1771px">Archives</h3>
  <div class="widget-rule" style="top:1795px"></div>
  <ul class="side-list" style="top:1796px;--step:32.6px">
    <li>June 2013</li><li>March 2013</li><li>February 2013</li><li>November 2012</li><li>October 2012</li><li>September 2012</li><li>August 2012</li><li>July 2012</li><li>May 2012</li>
  </ul>

  <h3 class="widget-title" style="top:2126px">Categories</h3>
  <div class="widget-rule" style="top:2150px"></div>
  <ul class="side-list" style="top:2151px;--step:30.9px">
    <li>art</li><li>Cityscapes</li><li>market</li><li>Other Work</li><li>Seascapes</li><li>social</li><li>wedding</li><li>work in progress</li>
  </ul>

  <h3 class="widget-title" style="top:2424px">Meta</h3>
  <div class="widget-rule" style="top:2448px"></div>
  <ul class="side-list" style="top:2468px;--step:31px">
    <li>Register</li><li>Log in</li><li>Entries RSS</li><li>Comments RSS</li><li>Blog at Inkpage.com.</li>
  </ul>

  <footer>
    <div class="footer-nav">Home<span class="sep">|</span>About<span class="sep">|</span>Cityscapes<span class="sep">|</span>Other Works<span class="sep">|</span>Seascapes<span class="sep">|</span>Testimonials<span class="sep">|</span>Works for Sale</div>
    <div class="copyright">Copyright ©2013 Company Name &nbsp;- All rights reserved</div>
  </footer>
</div>
</body>
</html>
```